Interior Plaster, Plasterboard Fixing & Installation Business CardDesign

TROVEL The name was formed by me, in talking to my accountant, whilst skim coating his walls and I had seen an imperfection in a wall that needed to be skim coated to deflect the light from the imperfection. I responded to him saying...."just Trov El". The idea originates from the process of applying a skim coat of interior plaster to a wall to achieve a smoother surface. This is required prior to many applications, applying wall paper, preparation for paint, after removing wall paper, improving aesthetics, joints that have not been properly jointed etc. Different types of light reflected on the surface, makes poor jointing more visible. In addition, the businesses key functions will be interior plastering, plaster board installation (ceilings and walls) and plasterboard jointing to a level that is prepared for a painter. Once the plaster is applied the surface requires sanding using different types of sanding equipment manual and electronic, including the use of specialised paint-on sealers for the surface. I believe the name is simple, easy to remember, but may be read incorrectly. I have had people ask if it was Trov El, referring to information technology.

For now, this entire concept is driven by passion and started 2 years ago whilst renovating my own home.

I need to be able to use your expertise to translate my ideas, starting with business card and progressing to a website incorporating anything and everything in between. The final design should be easy to understand, read and standout with an element of uniqueness. Humour maybe an option, or the idea of leaving a prospect with something that is thought provoking.
Updates

Hi All Ideas look fine so far, but would expect to see different colour options. I am thinking plaster thats cream in colour, so more earthy colour on the card. A picture of a trowel to replace the I in TROVEL maybe. I like the swirl that is created by a notched trowel moving through plaster. Perhaps a more modern or fresher look. With TROVEL, could you consider reversing the direction of the K for instance facing in the opposite direction. In saying this I look to you for your experience and expertise with the idea. The other option with the K, could be to remove the first straight line, i hope that my explanation helps. Sorry if it doesn't. Thanks heaps :)

Please include the type of service. Plasterboard Services

I have considered the idea of the K being reversed, and I am of the view that it presents a challenge reading and understanding. Moving forward I would however like to use the K in the normal direction but without the first straight line. I need to see more colour options that are grey or earthy. Can a picture of a trowel be included if it makes sense and with that tool being frequently used in plastering.

Industry/Entity Type

Business

Contact Information for Business Card

Company name: TrovEl
Name: Devon Marsh
Title: Director
Email address: marshdk@postvale.example
Mobile number: 0214 873 9012
Address: 17 Wexley Crescent, Fernhurst, Auckland, 0614

```html
<!DOCTYPE html>
<html lang="en">
<head>
<meta charset="utf-8">
<title>TROVEL — Plasterboard Services — Business Card</title>
<link rel="stylesheet" href="https://fonts.googleapis.com/css2?family=Jost:wght@600;700&display=swap">
<style>
  :root {
    --card-bg: #0e0e0f;
    --card-bg-light: #1b1b1c;
    --bar-white: #ffffff;
    --text-white: #ffffff;
    --accent-cyan: #62e4ea;
    --font-main: "Jost", "Century Gothic", Arial, sans-serif;
  }

  html, body {
    margin: 0;
    padding: 0;
    width: 1200px;
    height: 741px;
    overflow: hidden;
    background: var(--card-bg);
  }

  .card {
    position: relative;
    width: 1200px;
    height: 741px;
    overflow: hidden;
    font-family: var(--font-main);
    color: var(--text-white);
  }

  .card-texture {
    position: absolute;
    inset: 0;
    background: linear-gradient(135deg, var(--card-bg-light) 0%, var(--card-bg) 55%, var(--card-bg-light) 100%);
  }

  .side-bar {
    position: absolute;
    left: 189px;
    top: 0;
    width: 121px;
    height: 598px;
    background: var(--bar-white);
    border-radius: 0 0 8px 8px;
  }

  .brand-mark {
    position: absolute;
    left: 206px;
    top: 492px;
    width: 88px;
    height: 88px;
    border-radius: 50%;
    background: var(--accent-cyan);
  }

  .brand-name {
    position: absolute;
    left: 333px;
    top: 478px;
    margin: 0;
    font-size: 112px;
    font-weight: 700;
    line-height: 1;
    letter-spacing: 1px;
    color: var(--accent-cyan);
  }

  .service-type {
    position: absolute;
    left: 344px;
    top: 598px;
    margin: 0;
    font-size: 31px;
    font-weight: 600;
    line-height: 1;
    color: var(--text-white);
  }

  .holder-name {
    position: absolute;
    right: 109px;
    top: 81px;
    margin: 0;
    font-size: 32px;
    font-weight: 600;
    line-height: 1;
    letter-spacing: 0.5px;
  }

  .contact-list {
    position: absolute;
    right: 90px;
    top: 147px;
    margin: 0;
    padding: 0;
    list-style: none;
    text-align: right;
  }

  .contact-item {
    font-size: 22px;
    font-weight: 600;
    line-height: 28.5px;
    letter-spacing: 0.4px;
  }

  .contact-item::after {
    content: "";
    display: inline-block;
    width: 11px;
    height: 11px;
    margin-left: 8px;
    background: var(--accent-cyan);
    vertical-align: 1px;
  }
</style>
</head>
<body>
  <main class="card">
    <div class="card-texture" role="img" aria-label="Dark background with a subtle grid of grey squares"></div>

    <div class="side-bar"></div>

    <div class="brand-mark"></div>
    <h1 class="brand-name">TROVEL</h1>
    <p class="service-type">Plasterboard Services</p>

    <h2 class="holder-name">Devon Marsh</h2>
    <ul class="contact-list">
      <li class="contact-item">0214 873 9012</li>
      <li class="contact-item">marshdk@postvale.example</li>
      <li class="contact-item">17 Wexley Crescent, Fernhurst</li>
      <li class="contact-item">Auckland, 0614</li>
    </ul>
  </main>
</body>
</html>
```